Refresh Application User Interface

Brindlecove wishes to update the look of its business applications. Two representative forms are shown below. Please note, we are not considering changes in functionality or usability. Our goal is a cleaner, more contemporary design.

Industry/Entity Type

Business

```html
<!DOCTYPE html>
<html lang="en">
<head>
<meta charset="utf-8">
<title>Brindlecove – Purchase Order Lines</title>
<link href="https://fonts.googleapis.com/css2?family=Mulish:wght@300;400;600;700;800&display=swap" rel="stylesheet">
<style>
:root{
  --topbar:#3b3b3b;
  --topbar-hi:#5d5d5d;
  --blue:#3f8ee9;
  --blue-dark:#2f7ad6;
  --green:#1fb45a;
  --green-strip:#5fcf7a;
  --red:#e5302b;
  --bg:#ededed;
  --panel:#ffffff;
  --panel-soft:#f4f4f4;
  --line:#d6d6d6;
  --field:#f2f2f2;
  --text:#4a4a4a;
  --muted:#7b7b7b;
  --title:#6d7c8c;
}
*{box-sizing:border-box;margin:0;padding:0}
html,body{width:811px;height:1200px;overflow:hidden;background:var(--bg)}
body{font-family:"Mulish",sans-serif;color:var(--text);position:relative}
.viewport{position:absolute;left:0;top:0;width:811px;height:1200px;overflow:hidden}
.stage{position:absolute;left:0;top:0;width:1014px;height:1500px;overflow:hidden;transform:scale(0.8);transform-origin:0 0;background:var(--bg)}
.screen{position:absolute;left:0;width:1014px;height:750px;overflow:hidden}
.abs{position:absolute}
.topbar{left:0;top:0;width:1014px;height:32px;background:var(--topbar);color:#fff}
.user{left:11px;top:6px;font-size:15px;font-weight:600;white-space:nowrap}
.role{left:126px;top:9px;font-size:12px;font-weight:700;white-space:nowrap}
.topnav{top:0;height:32px;font-size:11px;line-height:32px;color:#ddd}
.topnav.hi{background:var(--topbar-hi)}
.appnav{left:0;top:32px;width:1014px;height:40px;background:#fff;border-bottom:1px solid var(--line)}
.apptab{top:0;height:40px;line-height:40px;text-align:center;font-size:10.5px;color:var(--muted);border-right:1px solid var(--line)}
.apptab.on{background:var(--blue);color:#fff;font-weight:700}
.brand{right:10px;top:9px;font-size:20px;font-weight:800;color:var(--blue-dark);letter-spacing:.5px;white-space:nowrap;text-align:right}
.subnav{left:0;top:72px;width:1014px;height:28px;background:var(--blue)}
.subitem{top:8px;font-size:9.5px;color:#fff;white-space:nowrap}
.subitem.on{font-weight:800;border-bottom:2px solid #fff;padding:0 18px 7px;left:107px}
.title{left:61px;top:130px;font-size:20px;color:var(--title);letter-spacing:.5px;font-weight:400}
.tab{top:125px;height:32px;background:#fff;border:1px solid var(--line);border-bottom:none;text-align:center;line-height:34px;font-size:12.5px;color:var(--muted)}
.tab.on{top:117px;height:40px;line-height:42px;background:var(--blue);color:#fff;font-weight:700;border:none}
.panel{left:60px;background:#fff;box-shadow:0 1px 3px rgba(0,0,0,.18)}
.toolbar{left:60px;top:158px;width:895px;height:28px;background:#fff;border-bottom:1px solid var(--line)}
.strip{width:8px;background:var(--green-strip)}
.tool{top:8px;font-size:10.5px;color:#333;white-space:nowrap}
.badge{left:65px;top:188px;width:90px;height:17px;background:var(--green-strip);color:#fff;font-size:9.5px;font-weight:700;text-align:center;line-height:17px}
.lbl{font-size:12.5px;color:var(--muted);text-align:right}
.box{height:21px;background:var(--field);border:1px solid #dcdcdc;font-size:11px;line-height:19px;padding-left:7px;color:#444;white-space:nowrap;overflow:hidden}
.link{font-size:10px;color:#555;text-decoration:underline}
.sub{top:398px;height:24px;background:var(--blue);color:#fff;font-size:11px;font-weight:700;text-align:center;line-height:26px}
.sub.on{top:392px;height:32px;background:#fff;color:var(--muted);font-weight:400;font-size:13px;line-height:34px;border:1px solid var(--line);border-bottom:none}
.shipzone{left:60px;top:422px;width:895px;height:273px;background:var(--panel-soft);border-top:1px solid var(--line)}
.flbl{font-size:9px;color:#555}
.sel{height:20px;border-bottom:1px solid #d0d0d0;background:#fff;font-size:11px;color:#666;padding-left:9px;line-height:20px}
.sel::after{content:"";position:absolute;right:9px;top:8px;border:4px solid transparent;border-top:5px solid #999}
.req{color:var(--red);font-size:12px}
.status{left:60px;width:895px;height:23px;background:#fff;font-size:10.5px;color:#555;line-height:23px;padding-left:24px;white-space:nowrap}
.status .strip{position:absolute;left:0;top:0;height:23px}
.ok{color:var(--green)}
.center{left:60px;top:185px;width:895px;height:137px;background:var(--panel-soft);text-align:center}
.gridbar{left:60px;top:325px;width:895px;height:28px;background:#fff;border-bottom:1px solid var(--line)}
.gh{top:360px;font-size:10.5px;color:#555;white-space:nowrap}
.ln{font-size:12.5px;color:var(--blue)}
.in{height:18px;border:1px solid #d4d4d4;background:#fff;font-size:10px;line-height:16px;padding-left:6px;color:#555}
.dd{height:18px;border:1px solid #d4d4d4;background:#fff}
.dd::after{content:"";position:absolute;right:6px;top:6px;border:4px solid transparent;border-top:5px solid #999}
.cb{width:13px;height:13px;border:1px solid #b7b7b7;background:#fff}
.desc{height:18px;border:1px solid #d4d4d4;background:#fff;font-size:9.5px;line-height:16px;padding-left:7px;color:#555;white-space:nowrap;overflow:hidden}
.note{font-size:10px;color:#444;white-space:nowrap}
</style>
</head>
<body>
<div class="viewport">
<div class="stage">

<!-- Header form -->
<section class="screen" style="top:0">
  <div class="abs topbar">
    <div class="abs user">Dana Keller <svg width="15" height="15" viewBox="0 0 16 16" style="vertical-align:-2px"><circle cx="8" cy="8" r="5.5" fill="none" stroke="#fff" stroke-width="3" stroke-dasharray="2.2 1.3"/><circle cx="8" cy="8" r="2" fill="#fff"/></svg></div>
    <div class="abs role">Administrator ⌄</div>
    <div class="abs topnav" style="left:677px">TOUCH</div>
    <div class="abs topnav hi" style="left:730px;width:79px;text-align:center">NEW TAB</div>
    <div class="abs topnav" style="left:828px">HELP</div>
    <div class="abs topnav" style="left:891px">SUPPORT</div>
    <svg class="abs" style="left:988px;top:7px" width="18" height="18" viewBox="0 0 18 18"><rect x="2" y="2" width="8" height="14" fill="none" stroke="#fff" stroke-width="1.8"/><path d="M9 9h8M14 6l3 3-3 3" stroke="#fff" stroke-width="1.8" fill="none"/></svg>
  </div>
  <nav class="abs appnav">
    <div class="abs apptab" style="left:0;width:81px">Home</div>
    <div class="abs apptab" style="left:81px;width:93px">eSource</div>
    <div class="abs apptab on" style="left:174px;width:76px">eBuy</div>
    <div class="abs apptab" style="left:250px;width:101px">eRequest</div>
    <div class="abs apptab" style="left:351px;width:75px">eSell</div>
    <div class="abs apptab" style="left:426px;width:85px">eStock</div>
    <div class="abs apptab" style="left:511px;width:80px">ePlan</div>
    <div class="abs apptab" style="left:591px;width:110px">Preferences</div>
    <div class="abs brand">BRINDLECOVE</div>
  </nav>
  <nav class="abs subnav">
    <div class="abs subitem on">Orders</div>
    <div class="abs subitem" style="left:195px">Recepients</div>
    <div class="abs subitem" style="left:283px">Shipments</div>
    <div class="abs subitem" style="left:369px">Invoices</div>
    <div class="abs" style="left:432px;top:8px;width:1px;height:12px;background:#fff"></div>
    <div class="abs subitem" style="left:453px">Pricing</div>
    <div class="abs subitem" style="left:522px">Tables</div>
    <div class="abs subitem" style="left:589px">Reports</div>
    <div class="abs subitem" style="left:663px">Inquiries</div>
    <div class="abs subitem" style="left:740px">Periodic Tasks</div>
    <div class="abs subitem" style="left:842px">Workflows</div>
  </nav>

  <h1 class="abs title">PURCHASE ORDER LINES</h1>
  <div class="abs tab on" style="left:619px;width:92px">HEADER</div>
  <div class="abs tab" style="left:713px;width:80px">LINES</div>
  <div class="abs tab" style="left:793px;width:81px">CHARGES</div>
  <div class="abs tab" style="left:874px;width:81px">NOTES</div>
  <svg class="abs" style="left:937px;top:128px" width="13" height="13" viewBox="0 0 13 13"><circle cx="6.5" cy="6.5" r="6" fill="var(--green)"/><path d="M3.5 6.5l2 2 4-4" stroke="#fff" stroke-width="1.6" fill="none"/></svg>

  <div class="abs panel" style="top:157px;width:895px;height:538px"></div>
  <div class="abs toolbar">
    <div class="abs strip" style="left:0;top:0;height:28px"></div>
    <svg class="abs" style="left:31px;top:8px" width="12" height="13" viewBox="0 0 12 13"><path d="M8 4L4 8.5a1.5 1.5 0 002 2L10.5 6a2.7 2.7 0 00-4-4L2 6.5" stroke="var(--green)" stroke-width="1.4" fill="none"/></svg>
    <svg class="abs" style="left:67px;top:8px" width="14" height="13" viewBox="0 0 14 13"><path d="M2 2h6l5 5-5 5-5-5z" fill="none" stroke="#333" stroke-width="1.4"/><circle cx="5" cy="5" r="1.2" fill="#333"/></svg>
    <svg class="abs" style="left:104px;top:8px" width="14" height="13" viewBox="0 0 14 13"><circle cx="3" cy="9" r="2" fill="#333"/><circle cx="7" cy="3" r="2" fill="#333"/><circle cx="11" cy="9" r="2" fill="#333"/><path d="M3 9L7 3l4 6" stroke="#333" fill="none"/></svg>
    <svg class="abs" style="left:142px;top:8px" width="14" height="12" viewBox="0 0 14 12"><rect x="1" y="3" width="12" height="8" fill="#333"/><rect x="5" y="1" width="4" height="3" fill="none" stroke="#333"/></svg>
    <svg class="abs" style="left:179px;top:8px" width="12" height="12" viewBox="0 0 12 12"><circle cx="6" cy="6" r="5.5" fill="#ccc"/><text x="6" y="9" font-size="8" text-anchor="middle" fill="#fff">?</text></svg>
    <div class="abs" style="left:208px;top:5px;width:1px;height:18px;background:var(--line)"></div>
    <div class="abs tool" style="left:224px"><svg width="12" height="11" viewBox="0 0 12 11" style="vertical-align:-1px"><rect width="12" height="11" fill="#333"/><rect x="3" y="3" width="6" height="5" fill="#fff"/></svg> Post Order</div>
    <svg class="abs" style="left:748px;top:8px" width="13" height="13" viewBox="0 0 13 13"><circle cx="5" cy="5" r="3.8" stroke="#bbb" stroke-width="1.6" fill="none"/><path d="M8 8l4 4" stroke="#bbb" stroke-width="1.8"/></svg>
    <svg class="abs" style="left:777px;top:8px" width="12" height="12" viewBox="0 0 12 12"><path d="M6 0v12M0 6h12" stroke="#bbb" stroke-width="2"/></svg>
    <svg class="abs" style="left:805px;top:7px" width="15" height="13" viewBox="0 0 15 13"><path d="M1 7l4 4 9-10" stroke="var(--green)" stroke-width="2.2" fill="none"/></svg>
    <svg class="abs" style="left:837px;top:8px" width="12" height="12" viewBox="0 0 12 12"><path d="M1 1l10 10M11 1L1 11" stroke="var(--red)" stroke-width="2.4"/></svg>
    <svg class="abs" style="left:865px;top:8px" width="13" height="12" viewBox="0 0 13 12"><path d="M3 2h5a3.5 3.5 0 010 7H2M4 6.5L1.5 9 4 11.5" stroke="var(--green)" stroke-width="1.6" fill="none"/></svg>
  </div>
  <div class="abs badge">Attachments</div>

  <div class="abs" style="left:124px;top:218px;font-size:12.5px;color:var(--muted)">Order # &nbsp;<span style="color:#555">100159</span></div>

  <div class="abs lbl" style="left:90px;top:263px;width:80px">Ship From</div>
  <div class="abs box" style="left:181px;top:260px;width:118px">1001</div>
  <div class="abs" style="left:310px;top:261px;color:#777">/</div>
  <div class="abs box" style="left:327px;top:260px;width:42px">0</div>
  <div class="abs box" style="left:181px;top:285px;width:293px">Harbor Clinical Supply</div>
  <div class="abs lbl" style="left:90px;top:313px;width:80px">Address</div>
  <div class="abs box" style="left:181px;top:310px;width:293px">14 Tidewater Lane</div>
  <div class="abs box" style="left:181px;top:334px;width:293px"></div>

  <div class="abs lbl" style="left:500px;top:264px;width:86px">City</div>
  <div class="abs box" style="left:596px;top:260px;width:184px">Northcliff</div>
  <div class="abs lbl" style="left:500px;top:288px;width:86px">State</div>
  <div class="abs box" style="left:596px;top:284px;width:184px">MA</div>
  <div class="abs lbl" style="left:500px;top:313px;width:86px">Country</div>
  <div class="abs box" style="left:596px;top:309px;width:184px">United States</div>
  <div class="abs lbl" style="left:500px;top:337px;width:86px">ZIP</div>
  <div class="abs box" style="left:596px;top:333px;width:184px">01820-4410</div>
  <div class="abs" style="left:795px;top:289px;font-size:10.5px;color:#666;white-space:nowrap"><span class="cb" style="display:inline-block;vertical-align:-2px;width:12px;height:12px;position:relative"><svg style="position:absolute;left:1px;top:0" width="10" height="10" viewBox="0 0 10 10"><path d="M1 5l3 3 5-7" stroke="#444" stroke-width="1.3" fill="none"/></svg></span> Accept</div>
  <div class="abs link" style="left:795px;top:336px">Add Contact</div>

  <div class="abs sub" style="left:60px;width:135px">ORDER INFO</div>
  <div class="abs sub on" style="left:198px;width:136px">SHIPPING</div>
  <div class="abs sub" style="left:335px;width:136px">PAYMENT</div>
  <div class="abs sub" style="left:473px;width:136px">ACCOUNTS</div>
  <div class="abs sub" style="left:611px;width:137px">TOTALS / APPROVAL</div>

  <div class="abs shipzone"></div>
  <div class="abs flbl" style="left:166px;top:441px">Receive At</div>
  <div class="abs sel" style="left:166px;top:454px;width:152px">ALCH</div><div class="abs req" style="left:326px;top:457px">*</div>
  <div class="abs flbl" style="left:166px;top:481px">Carrier</div>
  <div class="abs sel" style="left:166px;top:494px;width:152px">ParcelLine</div><div class="abs req" style="left:326px;top:497px">*</div>
  <div class="abs flbl" style="left:166px;top:521px">Express Service</div>
  <div class="abs sel" style="left:166px;top:533px;width:152px"></div>
  <div class="abs flbl" style="left:166px;top:561px">FOB</div>
  <div class="abs sel" style="left:166px;top:573px;width:152px"></div>
  <div class="abs flbl" style="left:166px;top:601px">Order Ship Rule</div>
  <div class="abs sel" style="left:166px;top:613px;width:223px">Partials</div><div class="abs req" style="left:397px;top:617px">*</div>
  <div class="abs flbl" style="left:166px;top:642px">Line Ship Rule</div>
  <div class="abs sel" style="left:166px;top:655px;width:223px">Partials</div><div class="abs req" style="left:397px;top:660px">*</div>

  <div class="abs flbl" style="left:441px;top:441px">Request Date</div>
  <div class="abs" style="left:441px;top:454px;width:136px;height:20px;background:#fff;border-bottom:1px solid #d0d0d0"></div>
  <svg class="abs" style="left:581px;top:451px" width="20" height="21" viewBox="0 0 20 21"><rect x="1" y="3" width="18" height="17" fill="#3a8de0"/><rect x="4" y="0" width="2" height="5" fill="#3a8de0"/><rect x="14" y="0" width="2" height="5" fill="#3a8de0"/><g fill="#fff"><rect x="4" y="9" width="3" height="3"/><rect x="8.5" y="9" width="3" height="3"/><rect x="13" y="9" width="3" height="3"/><rect x="4" y="14" width="3" height="3"/><rect x="8.5" y="14" width="3" height="3"/><rect x="13" y="14" width="3" height="3"/></g></svg>
  <div class="abs flbl" style="left:441px;top:481px">Freight Terms</div>
  <div class="abs sel" style="left:441px;top:494px;width:160px">Collect</div>
  <div class="abs flbl" style="left:441px;top:521px">Freight Calc</div>
  <div class="abs sel" style="left:441px;top:533px;width:160px"></div>

  <div class="abs flbl" style="left:700px;top:441px">Customer Ship To</div>
  <div class="abs box" style="left:700px;top:453px;width:87px;height:20px"></div>
  <div class="abs" style="left:797px;top:453px;color:#555">/</div>
  <div class="abs box" style="left:812px;top:453px;width:37px;height:20px"></div>

  <div class="abs status" style="top:710px"><span class="strip"></span>Enter property values, and click <span class="ok">✓</span> Apply</div>
</section>

<!-- Lines form -->
<section class="screen" style="top:750px">
  <div class="abs topbar">
    <div class="abs user">Dana Keller <svg width="15" height="15" viewBox="0 0 16 16" style="vertical-align:-2px"><circle cx="8" cy="8" r="5.5" fill="none" stroke="#fff" stroke-width="3" stroke-dasharray="2.2 1.3"/><circle cx="8" cy="8" r="2" fill="#fff"/></svg></div>
    <div class="abs role">Administrator ⌄</div>
    <div class="abs topnav" style="left:677px">TOUCH</div>
    <div class="abs topnav hi" style="left:730px;width:79px;text-align:center">NEW TAB</div>
    <div class="abs topnav" style="left:828px">HELP</div>
    <div class="abs topnav" style="left:891px">SUPPORT</div>
    <svg class="abs" style="left:988px;top:7px" width="18" height="18" viewBox="0 0 18 18"><rect x="2" y="2" width="8" height="14" fill="none" stroke="#fff" stroke-width="1.8"/><path d="M9 9h8M14 6l3 3-3 3" stroke="#fff" stroke-width="1.8" fill="none"/></svg>
  </div>
  <nav class="abs appnav">
    <div class="abs apptab" style="left:0;width:81px">Home</div>
    <div class="abs apptab" style="left:81px;width:93px">eSource</div>
    <div class="abs apptab on" style="left:174px;width:76px">eBuy</div>
    <div class="abs apptab" style="left:250px;width:101px">eRequest</div>
    <div class="abs apptab" style="left:351px;width:75px">eSell</div>
    <div class="abs apptab" style="left:426px;width:85px">eStock</div>
    <div class="abs apptab" style="left:511px;width:80px">ePlan</div>
    <div class="abs apptab" style="left:591px;width:110px">Preferences</div>
    <div class="abs brand">BRINDLECOVE</div>
  </nav>
  <nav class="abs subnav">
    <div class="abs subitem on">Orders</div>
    <div class="abs subitem" style="left:195px">Recepients</div>
    <div class="abs subitem" style="left:283px">Shipments</div>
    <div class="abs subitem" style="left:369px">Invoices</div>
    <div class="abs" style="left:432px;top:8px;width:1px;height:12px;background:#fff"></div>
    <div class="abs subitem" style="left:453px">Pricing</div>
    <div class="abs subitem" style="left:522px">Tables</div>
    <div class="abs subitem" style="left:589px">Reports</div>
    <div class="abs subitem" style="left:663px">Inquiries</div>
    <div class="abs subitem" style="left:740px">Periodic Tasks</div>
    <div class="abs subitem" style="left:842px">Workflows</div>
  </nav>

  <h1 class="abs title">PURCHASE ORDER LINES</h1>
  <div class="abs tab" style="left:619px;width:80px">HEADER</div>
  <div class="abs tab on" style="left:700px;width:92px">LINES</div>
  <div class="abs tab" style="left:793px;width:81px">CHARGES</div>
  <div class="abs tab" style="left:874px;width:81px">NOTES</div>
  <svg class="abs" style="left:937px;top:128px" width="13" height="13" viewBox="0 0 13 13"><circle cx="6.5" cy="6.5" r="6" fill="var(--green)"/><path d="M3.5 6.5l2 2 4-4" stroke="#fff" stroke-width="1.6" fill="none"/></svg>

  <div class="abs panel" style="top:157px;width:895px;height:538px"></div>
  <div class="abs toolbar">
    <div class="abs strip" style="left:0;top:0;height:28px"></div>
    <svg class="abs" style="left:31px;top:8px" width="12" height="13" viewBox="0 0 12 13"><path d="M8 4L4 8.5a1.5 1.5 0 002 2L10.5 6a2.7 2.7 0 00-4-4L2 6.5" stroke="#333" stroke-width="1.4" fill="none"/></svg>
    <svg class="abs" style="left:67px;top:8px" width="14" height="13" viewBox="0 0 14 13"><path d="M2 2h6l5 5-5 5-5-5z" fill="none" stroke="#333" stroke-width="1.4"/><circle cx="5" cy="5" r="1.2" fill="#333"/></svg>
    <svg class="abs" style="left:104px;top:8px" width="14" height="13" viewBox="0 0 14 13"><circle cx="3" cy="9" r="2" fill="#333"/><circle cx="7" cy="3" r="2" fill="#333"/><circle cx="11" cy="9" r="2" fill="#333"/><path d="M3 9L7 3l4 6" stroke="#333" fill="none"/></svg>
    <svg class="abs" style="left:142px;top:8px" width="14" height="12" viewBox="0 0 14 12"><rect x="1" y="3" width="12" height="8" fill="#333"/><rect x="5" y="1" width="4" height="3" fill="none" stroke="#333"/></svg>
    <svg class="abs" style="left:179px;top:8px" width="12" height="12" viewBox="0 0 12 12"><circle cx="6" cy="6" r="5.5" fill="#ccc"/><text x="6" y="9" font-size="8" text-anchor="middle" fill="#fff">?</text></svg>
    <div class="abs" style="left:208px;top:5px;width:1px;height:18px;background:var(--line)"></div>
    <div class="abs tool" style="left:224px"><svg width="13" height="12" viewBox="0 0 13 12" style="vertical-align:-1px"><path d="M1 1l11 10M12 1L1 11" stroke="#333" stroke-width="1.6"/></svg> View GL Accounts</div>
    <div class="abs tool" style="left:350px"><svg width="12" height="11" viewBox="0 0 12 11" style="vertical-align:-1px"><rect width="12" height="11" fill="#333"/><rect x="3" y="3" width="6" height="5" fill="#fff"/></svg> Post Order</div>
    <svg class="abs" style="left:748px;top:8px" width="13" height="13" viewBox="0 0 13 13"><circle cx="5" cy="5" r="3.8" stroke="var(--blue)" stroke-width="1.6" fill="none"/><path d="M8 8l4 4" stroke="var(--blue)" stroke-width="1.8"/></svg>
    <svg class="abs" style="left:777px;top:8px" width="12" height="12" viewBox="0 0 12 12"><path d="M6 0v12M0 6h12" stroke="#bbb" stroke-width="2"/></svg>
    <svg class="abs" style="left:805px;top:7px" width="15" height="13" viewBox="0 0 15 13"><path d="M1 7l4 4 9-10" stroke="var(--green)" stroke-width="2.2" fill="none"/></svg>
    <svg class="abs" style="left:837px;top:8px" width="12" height="12" viewBox="0 0 12 12"><path d="M1 1l10 10M11 1L1 11" stroke="var(--red)" stroke-width="2.4"/></svg>
    <svg class="abs" style="left:865px;top:8px" width="13" height="12" viewBox="0 0 13 12"><path d="M3 2h5a3.5 3.5 0 010 7H2M4 6.5L1.5 9 4 11.5" stroke="var(--green)" stroke-width="1.6" fill="none"/></svg>
  </div>

  <div class="abs center">
    <div style="margin-top:26px;font-size:12.5px;color:var(--muted)">Order # &nbsp;100159</div>
    <div style="margin-top:6px;font-size:17px;font-weight:700;color:var(--green)">Regular Purchase Order</div>
    <div style="margin-top:26px;font-size:12px;color:#555">Harbor Clinical Supply, Northcliff MA</div>
  </div>

  <div class="abs gridbar">
    <div class="abs" style="left:0;top:0;width:8px;height:28px;background:var(--blue)"></div>
    <div class="abs" style="left:31px;top:4px;font-size:14px;color:#333">Σ</div>
    <svg class="abs" style="left:68px;top:7px" width="12" height="13" viewBox="0 0 12 13"><rect x="1" y="3" width="7" height="9" fill="none" stroke="#333" stroke-width="1.3"/><rect x="4" y="1" width="7" height="9" fill="#fff" stroke="#333" stroke-width="1.3"/></svg>
    <svg class="abs" style="left:105px;top:7px" width="12" height="13" viewBox="0 0 12 13"><rect x="1" y="1" width="10" height="11" fill="none" stroke="#333" stroke-width="1.3"/><rect x="5" y="1" width="6" height="11" fill="#333"/></svg>
    <svg class="abs" style="left:141px;top:7px" width="14" height="13" viewBox="0 0 14 13"><path d="M1 1h12L8.5 6.5V12h-3V6.5z" fill="#333"/></svg>
    <svg class="abs" style="left:180px;top:7px" width="13" height="13" viewBox="0 0 13 13"><path d="M1.5 1.5l10 10M11.5 1.5l-10 10" stroke="var(--red)" stroke-width="2.6"/></svg>
    <svg class="abs" style="left:656px;top:8px" width="12" height="12" viewBox="0 0 12 12"><rect x="1" y="1" width="2" height="10" fill="#aaa"/><path d="M11 1v10L4 6z" fill="#aaa"/></svg>
    <svg class="abs" style="left:691px;top:8px" width="16" height="12" viewBox="0 0 16 12"><path d="M8 1v10L1 6zM15 1v10L8 6z" fill="#aaa"/></svg>
    <div class="abs" style="left:738px;top:8px;font-size:11px;color:#555;white-space:nowrap">Page 1 of 1</div>
    <svg class="abs" style="left:827px;top:8px" width="16" height="12" viewBox="0 0 16 12"><path d="M1 1v10l7-5zM8 1v10l7-5z" fill="#aaa"/></svg>
    <svg class="abs" style="left:865px;top:8px" width="12" height="12" viewBox="0 0 12 12"><path d="M1 1v10l7-5z" fill="#aaa"/><rect x="9" y="1" width="2" height="10" fill="#aaa"/></svg>
  </div>

  <div class="abs gh" style="left:74px">Line #</div>
  <div class="abs gh" style="left:134px">Product</div>
  <div class="abs gh" style="left:268px">Supplier Part #</div>
  <div class="abs gh" style="left:378px">Open Qty</div>
  <div class="abs gh" style="left:472px">Unit</div>
  <div class="abs gh" style="left:565px">Unit Price</div>
  <div class="abs gh" style="left:656px">Extended</div>
  <div class="abs gh" style="left:753px">LI Type / Ship To</div>
  <div class="abs cb" style="left:917px;top:360px"></div>

  <div class="abs ln" style="left:74px;top:403px">10</div>
  <div class="abs in" style="left:129px;top:401px;width:120px">P-1200</div>
  <svg class="abs" style="left:252px;top:402px" width="14" height="14" viewBox="0 0 14 14"><circle cx="8" cy="6" r="4" stroke="var(--blue)" stroke-width="1.8" fill="none"/><path d="M5 9l-4 4" stroke="var(--blue)" stroke-width="2"/></svg>
  <div class="abs cb" style="left:282px;top:403px"></div>
  <div class="abs in" style="left:375px;top:401px;width:68px">1</div>
  <div class="abs dd" style="left:469px;top:401px;width:69px"></div>
  <div class="abs" style="left:553px;top:401px;font-size:12px;color:#555">$</div>
  <div class="abs in" style="left:564px;top:401px;width:68px">6.50</div>
  <div class="abs dd" style="left:751px;top:401px;width:137px"></div>
  <div class="abs cb" style="left:917px;top:403px"></div>
  <div class="abs desc" style="left:129px;top:423px;width:503px">Papermark 389317 - Brochure Paper, Ultra Smooth Text, 8 1/2" x 11", 28 lb., 96 Brightness</div>
  <div class="abs dd" style="left:751px;top:423px;width:137px"></div>
  <div class="abs note" style="left:183px;top:451px">On Purchase Order &nbsp;<span style="color:var(--blue)">30</span></div>
  <div class="abs note" style="left:378px;top:451px">Available &nbsp;0</div>
  <div class="abs" style="left:566px;top:450px;font-size:10px;font-style:italic;color:var(--red);white-space:nowrap">Over Budget</div>

  <div class="abs" style="left:60px;top:473px;width:895px;height:1px;background:#eee"></div>

  <div class="abs ln" style="left:74px;top:488px">20</div>
  <div class="abs in" style="left:129px;top:486px;width:120px">P-1200</div>
  <svg class="abs" style="left:252px;top:487px" width="14" height="14" viewBox="0 0 14 14"><circle cx="8" cy="6" r="4" stroke="var(--blue)" stroke-width="1.8" fill="none"/><path d="M5 9l-4 4" stroke="var(--blue)" stroke-width="2"/></svg>
  <div class="abs cb" style="left:282px;top:488px"></div>
  <div class="abs in" style="left:375px;top:486px;width:68px">1</div>
  <div class="abs dd" style="left:469px;top:486px;width:69px"></div>
  <div class="abs" style="left:553px;top:486px;font-size:12px;color:#555">$</div>
  <div class="abs in" style="left:564px;top:486px;width:68px">6.50</div>
  <div class="abs dd" style="left:751px;top:486px;width:137px"></div>
  <div class="abs cb" style="left:917px;top:488px"></div>
  <div class="abs desc" style="left:129px;top:508px;width:503px">Papermark 389317 - Brochure Paper, Ultra Smooth Text, 8 1/2" x 11", 28 lb., 96 Brightness</div>
  <div class="abs dd" style="left:751px;top:508px;width:137px"></div>

  <div class="abs" style="left:60px;top:560px;width:895px;height:1px;background:#eee"></div>

  <div class="abs ln" style="left:74px;top:573px">20</div>
  <div class="abs in" style="left:129px;top:571px;width:120px"></div>
  <svg class="abs" style="left:252px;top:572px" width="14" height="14" viewBox="0 0 14 14"><circle cx="8" cy="6" r="4" stroke="var(--blue)" stroke-width="1.8" fill="none"/><path d="M5 9l-4 4" stroke="var(--blue)" stroke-width="2"/></svg>
  <div class="abs cb" style="left:282px;top:573px"></div>
  <div class="abs in" style="left:375px;top:571px;width:68px"></div>
  <div class="abs dd" style="left:469px;top:571px;width:69px"></div>
  <div class="abs" style="left:553px;top:571px;font-size:12px;color:#555">$</div>
  <div class="abs in" style="left:564px;top:571px;width:68px"></div>
  <div class="abs dd" style="left:751px;top:571px;width:137px"></div>
  <div class="abs desc" style="left:129px;top:593px;width:503px"></div>
  <div class="abs dd" style="left:751px;top:593px;width:137px"></div>

  <div class="abs status" style="top:710px"><span class="strip"></span>Click <svg width="12" height="12" viewBox="0 0 13 13" style="vertical-align:-2px"><circle cx="5" cy="5" r="3.8" stroke="var(--blue)" stroke-width="1.6" fill="none"/><path d="M8 8l4 4" stroke="var(--blue)" stroke-width="1.8"/></svg>Search, or enter property values and click <span class="ok">✓</span> Apply</div>
</section>

</div>
</div>
</body>
</html>
```